New business card design for Pinecrest Hollow Optometry Clinic

We need a new business card design using our existing logo (uploaded). Please do not include eyes, eye exam charts or beaches, water, sand. The logo I uploaded shows our colors of green and blue, but we are open to seeing it in black OR white. We would like to see something modern and fresh. It will need to be 2 sided. On the front we will need to be able to put a doctors name, for example-Dr Marta Kellerman and Associates. We will need to be able to change the name to other doctors names when we send for printing. The back of the card should list the following: 3817 Tarrow St, Alder Cove (P)705-555-0148 (E) info@phoc.ca www.phoc.ca. "We are welcoming new patients" and a line for the appointment date and time. I have uploaded the back of a card to give an example

```html
<!DOCTYPE html>
<html lang="en">
<head>
<meta charset="UTF-8">
<title>Pinecrest Hollow Optometry Clinic – Business Card</title>
<link href="https://fonts.googleapis.com/css2?family=Montserrat:wght@500;600;700&display=swap" rel="stylesheet">
<style>
  :root {
    --canvas: #d4d4d4;
    --card: #ffffff;
    --ink: #111111;
    --band: #000000;
    --band-text: #ffffff;
    --shadow: rgba(0, 0, 0, 0.35);
  }
  * { margin: 0; padding: 0; box-sizing: border-box; }
  html, body {
    width: 1200px;
    height: 1000px;
    overflow: hidden;
    background: var(--canvas);
    font-family: "Montserrat", Arial, sans-serif;
    color: var(--ink);
  }
  .canvas { position: relative; width: 1200px; height: 1000px; }
  .card {
    position: absolute;
    left: 265px;
    width: 670px;
    height: 382px;
    background: var(--card);
    box-shadow: 4px 8px 14px var(--shadow);
    overflow: hidden;
  }
  .card--front { top: 84px; }
  .card--back { top: 534px; }

  .brand-mark {
    position: absolute;
    top: 74px;
    left: 0;
    width: 100%;
    text-align: center;
    font-size: 136px;
    font-weight: 600;
    line-height: 1;
    letter-spacing: 4px;
  }
  .brand-name {
    position: absolute;
    top: 206px;
    left: 0;
    width: 100%;
    text-align: center;
    font-size: 24px;
    font-weight: 700;
    letter-spacing: -0.3px;
  }
  .divider {
    position: absolute;
    top: 270px;
    left: 0;
    width: 100%;
    height: 4px;
    background: var(--ink);
  }
  .doctor-name {
    position: absolute;
    top: 303px;
    left: 0;
    width: 100%;
    text-align: center;
    font-size: 24.5px;
    font-weight: 600;
  }

  .welcome-band {
    position: absolute;
    top: 0;
    left: 0;
    width: 100%;
    height: 114px;
    background: var(--band);
    color: var(--band-text);
    display: flex;
    align-items: center;
    justify-content: center;
    font-size: 29px;
    font-weight: 700;
    padding-top: 6px;
  }
  .contact-line {
    position: absolute;
    top: 135px;
    left: 0;
    width: 100%;
    display: flex;
    justify-content: center;
    align-items: center;
    gap: 10px;
    font-size: 20.5px;
    font-weight: 600;
  }
  .contact-item { display: flex; align-items: center; gap: 4px; }
  .contact-item svg { width: 19px; height: 19px; }
  .address {
    position: absolute;
    top: 167px;
    left: 0;
    width: 100%;
    text-align: center;
    font-size: 20.5px;
    font-weight: 600;
  }
  .appointment-field {
    position: absolute;
    display: flex;
    align-items: flex-end;
    font-size: 17px;
    font-weight: 500;
  }
  .field-rule {
    display: inline-block;
    height: 2px;
    background: var(--ink);
    margin-left: 6px;
    margin-bottom: 3px;
  }
  .field--doctor { top: 237px; left: 80px; }
  .field--doctor .field-rule { width: 439px; }
  .field--date { top: 304px; left: 80px; }
  .field--date .field-rule { width: 199px; margin-left: 5px; }
  .field--time { top: 304px; left: 334px; }
  .field--time .field-rule { width: 200px; margin-left: 8px; }
</style>
</head>
<body>
<main class="canvas">
  <section class="card card--front">
    <div class="brand-mark">PHOC</div>
    <div class="brand-name">Pinecrest Hollow Optometry Clinic</div>
    <div class="divider"></div>
    <div class="doctor-name">Dr Marta Kellerman and Associates</div>
  </section>

  <section class="card card--back">
    <div class="welcome-band">We are Welcoming New Patients!</div>
    <div class="contact-line">
      <span class="contact-item">
        <svg viewBox="0 0 20 20" aria-hidden="true"><circle cx="10" cy="10" r="9" fill="#111"/><path d="M6.5 5.2l2 .2.8 2.3-1.2 1a6 6 0 0 0 3.2 3.2l1-1.2 2.3.8.2 2c-.3.8-1.2 1.3-2 1.2A9 9 0 0 1 5.3 7.2c-.1-.8.4-1.7 1.2-2z" fill="#fff"/></svg>
        705-555-0148
      </span>
      <span class="contact-item">
        <svg viewBox="0 0 20 20" aria-hidden="true"><rect x="1" y="4" width="18" height="12" fill="#111"/><path d="M1.5 4.5L10 11l8.5-6.5M1.5 15.5l6-5.5M18.5 15.5l-6-5.5" stroke="#fff" stroke-width="1.4" fill="none"/></svg>
        info@phoc.ca
      </span>
      <span class="contact-item">
        <svg viewBox="0 0 20 20" aria-hidden="true" fill="none" stroke="#111" stroke-width="1.3"><circle cx="10" cy="10" r="8.5"/><ellipse cx="10" cy="10" rx="3.6" ry="8.5"/><path d="M1.5 10h17M3 5.5h14M3 14.5h14"/></svg>
        www.phoc.ca
      </span>
    </div>
    <div class="address">3817 Tarrow St, Alder Cove</div>

    <div class="appointment-field field--doctor">Doctor:<span class="field-rule"></span></div>
    <div class="appointment-field field--date">Date:<span class="field-rule"></span></div>
    <div class="appointment-field field--time">Time:<span class="field-rule"></span></div>
  </section>
</main>
</body>
</html>
```